Nera Bloom Fitness Coaching Project

I am a personal trainer based in London. My services include one-on-one PT sessions, bootcamps.
I would like the design to be minimalistic. With light colours: white, pink, purple.
I specialise in weight loss, flexibility, mobility.

Orla Pemvick
Personal Trainer
Email: orla.pemvick@tovamail.com
tel: 07400918243
Instagram: Nera Bloom

Target Market(s)

adults, mostly females (age 18-50).

Industry/Entity Type

Fitness

Contact Information for Business Card

Orla Pemvick
Personal Trainer
tel: 07400918243
Instagram: Nera Bloom

Font styles to use
Serif

Colors
eea4c8
fbd4d5
fdf9cf
cfeae6
cee9f5

Requirements
Nice to have
• minimalistic style
• easy to read and remember

```html
<!DOCTYPE html>
<html lang="en">
<head>
<meta charset="UTF-8">
<title>Orla Pemvick – Business Card</title>
<link href="https://fonts.googleapis.com/css2?family=Open+Sans:wght@400;600;700&display=swap" rel="stylesheet">
<style>
  :root {
    --stage-bg: #9a9a9a;
    --card-bg: #ffffff;
    --accent: #d12fc2;
    --accent-soft: rgba(209, 47, 194, 0.55);
    --text-grey: #6b6b6b;
    --photo-dark: #7a5a44;
    --photo-light: #d9c3a8;
    --frame: #1f1f1f;
  }
  * { margin: 0; padding: 0; box-sizing: border-box; }
  html, body {
    width: 1200px;
    height: 900px;
    overflow: hidden;
  }
  body {
    background: radial-gradient(ellipse at 50% 15%, #c4c4c4 0%, var(--stage-bg) 55%, #5e5e5e 100%);
    display: flex;
    align-items: center;
    justify-content: center;
    font-family: "Open Sans", Arial, sans-serif;
  }
  .business-card {
    width: 840px;
    height: 480px;
    background: var(--card-bg);
    box-shadow: 0 10px 30px rgba(0, 0, 0, 0.25);
    display: flex;
    flex-direction: column;
    align-items: center;
    padding-top: 56px;
    text-align: center;
  }
  .portrait {
    width: 136px;
    height: 136px;
    border-radius: 14px;
    border: 5px solid var(--frame);
    background: radial-gradient(circle at 50% 40%, var(--photo-light) 0%, var(--photo-dark) 75%);
  }
  .trainer-name {
    margin-top: 14px;
    font-size: 34px;
    font-weight: 700;
    color: var(--accent);
    letter-spacing: 0.5px;
    line-height: 1.1;
  }
  .trainer-role {
    font-size: 24px;
    font-weight: 400;
    color: var(--text-grey);
    letter-spacing: 0.5px;
    line-height: 1.2;
  }
  .divider {
    width: 640px;
    height: 2px;
    margin: 18px 0 14px;
    background: linear-gradient(90deg, transparent 0%, var(--accent-soft) 30%, var(--accent-soft) 70%, transparent 100%);
  }
  .divider--bottom { margin: 20px 0 0; }
  .contact-list {
    list-style: none;
    font-size: 22px;
    color: var(--text-grey);
    line-height: 1.45;
  }
  .social-line {
    display: inline-flex;
    align-items: center;
    gap: 8px;
  }
  .social-mark {
    width: 18px;
    height: 18px;
    border-radius: 3px;
    background: var(--accent);
  }
</style>
</head>
<body>
  <article class="business-card">
    <div class="portrait" role="img" aria-label="Portrait photo of Orla Pemvick"></div>
    <h1 class="trainer-name">ORLA PEMVICK</h1>
    <p class="trainer-role">PERSONAL TRAINER</p>
    <div class="divider"></div>
    <ul class="contact-list">
      <li>(P) 07400918243 (E) orla.pemvick@tovamail.com</li>
      <li class="social-line"><span class="social-mark"></span>Nera Bloom</li>
      <li>PT sessions, bootcamps.</li>
    </ul>
    <div class="divider divider--bottom"></div>
  </article>
</body>
</html>
```